Copperkettle Menu

I want to re design my menu at our restaurant Copperkettle, the current menu and information about the restaurant is online at www.copperkettle-eatery.example.nz, have attached the logo for Copperkettle as well as the new menu specifications

Menu design Specifications
· Rustic

· Raw

· Unpolished

· Urban

```html
<!DOCTYPE html>
<html lang="en">
<head>
<meta charset="utf-8">
<title>Copperkettle Menu</title>
<link href="https://fonts.googleapis.com/css2?family=PT+Sans:ital,wght@0,400;0,700;1,400&family=PT+Sans+Narrow:wght@700&family=Rye&display=swap" rel="stylesheet">
<style>
  :root {
    --paper: #a88a73;
    --ink: #3b2a20;
    --ornament: rgba(59, 42, 32, 0.16);
    --row: 18.4px;
  }
  * { margin: 0; padding: 0; box-sizing: border-box; }
  html, body { width: 760px; height: 1200px; overflow: hidden; background: var(--paper); }
  .menu-card {
    position: relative;
    width: 760px; height: 1200px;
    background: var(--paper);
    color: var(--ink);
    font-family: "PT Sans", Arial, sans-serif;
    font-size: 14px;
  }
  .corner-ornament {
    position: absolute; width: 108px; height: 108px;
    background: var(--ornament); border-radius: 6px;
  }
  .corner-ornament.top-left { left: 14px; top: 14px; }
  .corner-ornament.top-right { right: 14px; top: 14px; }
  .corner-ornament.bottom-left { left: 14px; bottom: 18px; }
  .corner-ornament.bottom-right { right: 14px; bottom: 18px; }

  .masthead-flourish {
    position: absolute; left: 244px; width: 296px;
    background: var(--ornament); border-radius: 30px;
  }
  .masthead-flourish.above { top: 30px; height: 42px; }
  .masthead-flourish.below { top: 128px; height: 58px; }
  .restaurant-name {
    position: absolute; left: 0; width: 760px; top: 74px;
    text-align: center;
    font-family: "PT Sans Narrow", "Arial Narrow", sans-serif;
    font-weight: 700; font-size: 44px; letter-spacing: 3px;
    line-height: 52px; text-transform: uppercase;
  }
  .menu-title {
    position: absolute; left: 104px; top: 172px;
    font-family: "Rye", Georgia, serif;
    font-size: 40px; line-height: 48px; letter-spacing: 1px;
  }

  .section { position: absolute; }
  .section-head {
    display: flex; align-items: flex-end;
    font-family: "PT Sans Narrow", "Arial Narrow", sans-serif;
    font-weight: 700; font-size: 16px; line-height: 20px;
  }
  .section-head .rule {
    flex: 1; border-bottom: 1.5px dashed var(--ink);
    margin: 0 2px 5px;
  }
  .section-head .note {
    font-family: "PT Sans", Arial, sans-serif; font-weight: 400; font-size: 14px;
  }
  .item { display: grid; height: var(--row); line-height: var(--row); white-space: nowrap; }
  .item .price { text-align: right; }
  .item .size { text-align: center; }

  .snacks { left: 104px; top: 225px; width: 526px; }
  .snacks .item { grid-template-columns: 1fr 30px; }

  .salads { left: 127px; top: 494px; }
  .salads .section-head { width: 489px; }
  .salads .item { grid-template-columns: 403px 28px 66px 28px; }

  .boards { left: 127px; width: 509px; }
  .boards .section-head { width: 455px; }
  .boards .item { grid-template-columns: 397px 28px 56px 28px; }
  .boards.first { top: 652px; }
  .boards.second { top: 787px; }

  .sweets { left: 104px; top: 920px; width: 527px; }
  .sweets .item { grid-template-columns: 1fr 30px; }

  .cheese { left: 116px; top: 1019px; width: 527px; }
  .cheese .item { grid-template-columns: 1fr 30px; }
  .cheese-note {
    position: absolute; left: 116px; top: 1113px;
    font-style: italic; font-size: 14px;
  }
</style>
</head>
<body>
<main class="menu-card">
  <div class="corner-ornament top-left" role="img" aria-label="Decorative scroll flourish in the corner"></div>
  <div class="corner-ornament top-right" role="img" aria-label="Decorative scroll flourish in the corner"></div>
  <div class="corner-ornament bottom-left" role="img" aria-label="Decorative scroll flourish in the corner"></div>
  <div class="corner-ornament bottom-right" role="img" aria-label="Decorative scroll flourish in the corner"></div>

  <div class="masthead-flourish above" role="img" aria-label="Decorative scrollwork above the restaurant name"></div>
  <h1 class="restaurant-name">Copperkettle</h1>
  <div class="masthead-flourish below" role="img" aria-label="Decorative scrollwork below the restaurant name"></div>

  <h2 class="menu-title">MENU</h2>

  <section class="section snacks">
    <div class="section-head"><span>Snacks</span><span class="rule"></span></div>
    <div class="item"><span>Pork crackling</span><span class="price">5</span></div>
    <div class="item"><span>Venison pasties &amp; plum sauce</span><span class="price">12</span></div>
    <div class="item"><span>Lamb Meat balls &amp; pomegranate molasses</span><span class="price">15</span></div>
    <div class="item"><span>Pulled pork &amp; apple slaw Sliders</span><span class="price">12</span></div>
    <div class="item"><span>Cheese fondue &amp; Asparagus</span><span class="price">10</span></div>
    <div class="item"><span>Battered fish fingers &amp; tartare sauce</span><span class="price">9</span></div>
    <div class="item"><span>Hand cut fries &amp; tomato sauce</span><span class="price">7</span></div>
    <div class="item"><span>Salmon &amp; avocado filled Sesame cones</span><span class="price">12</span></div>
    <div class="item"><span>Parmesan, chilli &amp; lemon Skinny fries</span><span class="price">7</span></div>
    <div class="item"><span>Barbequed Chicken tulips</span><span class="price">14</span></div>
    <div class="item"><span>Steamed mussels &amp; tomato salsa</span><span class="price">12</span></div>
    <div class="item"><span>Garlic bread</span><span class="price">6</span></div>
    <div class="item"><span>Crispy lentil balls &amp; roast garlic yoghurt</span><span class="price">8</span></div>
  </section>

  <section class="section salads">
    <div class="section-head"><span>Salads &amp; sides</span><span class="rule"></span><span class="note">sm or LG---</span></div>
    <div class="item"><span>Warmed Red skinned potatoes with dill &amp; mustard</span><span class="size">6</span><span></span><span class="size">9</span></div>
    <div class="item"><span>Tomato &amp; mixed beans</span><span class="size">8</span><span></span><span class="size">11</span></div>
    <div class="item"><span>Char grilled vegetables &amp; halloumi</span><span class="size">7</span><span></span><span class="size">10</span></div>
    <div class="item"><span>Orzo, broadbean &amp;feta</span><span class="size">7</span><span></span><span class="size">10</span></div>
    <div class="item"><span>Beetroot, spinach &amp; goats cheese with maple</span><span class="size">8</span><span></span><span class="size">11</span></div>
    <div class="item"><span>Mixed leaves &amp; citrus emulsion</span><span class="size">6</span><span></span><span class="size">9</span></div>
    <div class="item"><span>Steamed Broccoli &amp; sesame butter</span><span class="size">6</span><span></span><span class="size">9</span></div>
  </section>

  <section class="section boards first">
    <div class="section-head"><span>Boards + two sides</span><span class="rule"></span><span class="note">for one or two</span></div>
    <div class="item"><span>Beef wellington &amp; red wine jus</span><span class="size">36</span><span></span><span class="size">69</span></div>
    <div class="item"><span>Apricot glazed chicken crown</span><span class="size">34</span><span></span><span class="size">65</span></div>
    <div class="item"><span>Roast Pork scotch &amp; caramelised apple sauce</span><span class="size">32</span><span></span><span class="size">60</span></div>
    <div class="item"><span>Pan fried line caught fish &amp; lemon pickle</span><span class="size">35</span><span></span><span class="size">67</span></div>
    <div class="item"><span>Grilled lamb rack &amp; mint sauce</span><span class="size">38</span><span></span><span class="size">72</span></div>
    <div class="item"><span>Mixed roast nut loaf &amp; rhubarb marmalade</span><span class="size">28</span><span></span><span class="size">58</span></div>
  </section>

  <section class="section boards second">
    <div class="section-head"><span>Boards + two sides</span><span class="rule"></span><span class="note">for one or two</span></div>
    <div class="item"><span>Beef wellington &amp; red wine jus</span><span class="size">36</span><span></span><span class="size">69</span></div>
    <div class="item"><span>Apricot glazed chicken crown</span><span class="size">34</span><span></span><span class="size">65</span></div>
    <div class="item"><span>Roast Pork scotch &amp; caramelised apple sauce</span><span class="size">32</span><span></span><span class="size">60</span></div>
    <div class="item"><span>Pan fried line caught fish &amp; lemon pickle</span><span class="size">35</span><span></span><span class="size">67</span></div>
    <div class="item"><span>Grilled lamb rack &amp; mint sauce</span><span class="size">38</span><span></span><span class="size">72</span></div>
    <div class="item"><span>Mixed roast nut loaf &amp; rhubarb marmalade</span><span class="size">28</span><span></span><span class="size">58</span></div>
  </section>

  <section class="section sweets">
    <div class="section-head"><span>Sweets</span><span class="rule"></span></div>
    <div class="item"><span>Orange pannacotta with earl grey &amp; cardamom syrup</span><span class="price">12</span></div>
    <div class="item"><span>Chocolate terrine, macerated strawberries &amp; macadamia mascarpone</span><span class="price">14</span></div>
    <div class="item"><span>Vanilla bean crème brulee with cranberry &amp; pistachio biscotti</span><span class="price">12</span></div>
    <div class="item"><span>Pavolva roulade, kiwifruit, summer berries &amp; passionfruit cream</span><span class="price">12</span></div>
  </section>

  <section class="section cheese">
    <div class="section-head"><span>Cheese</span><span class="rule"></span></div>
    <div class="item"><span>Ridgeline aged cheddar</span><span class="price">16</span></div>
    <div class="item"><span>Hilltop triple Brie</span><span class="price">18</span></div>
    <div class="item"><span>Stonebridge Blue</span><span class="price">14</span></div>
  </section>
  <p class="cheese-note">with dried fruit, nuts, fruit paste and wafers</p>
</main>
</body>
</html>
```